Homepage for a Workout + Food Tracking Mobile App

We need a design for the homepage of our workout and food tracking app called FitKestra (working name, most likely not finalized). The app has many uses, namely a "Strength Review", food logging, workout tracking, statistics/analytics, an AI powered form review tool and an ability to ask an AI any workout, nutrition or app related questions. The homepage should feature some way to access the above listed features as well as an outline, 3d design, diagram or any other way to represent the human body split up into muscle groups for the user to see what muscles they've hit in any amount of time. There should be a section for a profile picture, username, "trophy case" with room for ideally 3 small "trophy" icons.
The main colour should be gold/dark yellow (I used #DEA30A) but I am very flexible on that and I'm curious to try out other colours. The background colour I am also flexible on, I went with a dark gray.
The screenshot I uploaded is in no way what your design needs to look like. Use it more to check what buttons and elements should be present.
I'll likely need more designs for other screens in the future and will be happy to work further with the designer chosen.
Target Market(s)
Gymgoers, People on a diet, Weightlifters,
Look and feel

```html
<!DOCTYPE html>
<html lang="en">
<head>
<meta charset="UTF-8">
<title>FitKestra – Home</title>
<link rel="stylesheet" href="https://fonts.googleapis.com/css2?family=Montserrat:wght@400;500;600;700&display=swap">
<style>
  :root {
    --canvas: #ececec;
    --gold: #f5b70f;
    --gold-deep: #e9a908;
    --gold-light: #fcc928;
    --ink: #1d1a12;
    --panel: #262626;
    --panel-dark: #1c1c1c;
    --band: #191919;
    --muted: #9a9a9a;
    --text-light: #d9d9d9;
  }
  * { box-sizing: border-box; margin: 0; padding: 0; }
  html, body { width: 1200px; height: 804px; overflow: hidden; }
  body {
    background: var(--canvas);
    font-family: "Montserrat", sans-serif;
    position: relative;
  }
  .screen {
    position: absolute;
    left: 435px; top: 12px;
    width: 330px; height: 780px;
    border-radius: 30px;
    overflow: hidden;
    background: var(--panel-dark);
  }
  .header {
    position: absolute; left: 0; top: 0; width: 330px; height: 212px;
    background: radial-gradient(circle at 100% 0%, var(--gold-light) 0%, var(--gold) 45%, var(--gold-deep) 100%);
  }
  .status-bar {
    position: absolute; left: 13px; right: 13px; top: 13px; height: 16px;
    display: flex; align-items: center; justify-content: space-between;
    font-size: 9px; font-weight: 600; color: var(--ink);
  }
  .notch {
    position: absolute; left: 143px; top: 17px; width: 44px; height: 9px;
    border-radius: 5px; background: var(--ink);
  }
  .status-icons { display: flex; gap: 5px; align-items: center; }
  .avatar {
    position: absolute; left: 13px; top: 54px; width: 70px; height: 70px;
    border-radius: 50%; border: 2px solid #fff;
    background: linear-gradient(135deg, #c99a6a, #8a5a3a 60%, #e2b27a);
  }
  .profile-name {
    position: absolute; left: 94px; top: 73px;
    font-size: 13px; font-weight: 600; color: var(--ink);
  }
  .profile-location {
    position: absolute; left: 95px; top: 96px;
    font-size: 9px; font-weight: 400; color: var(--ink);
  }
  .settings { position: absolute; left: 291px; top: 77px; }
  .trophy-case {
    position: absolute; left: 0; top: 136px; width: 330px; height: 70px;
    display: flex; justify-content: space-around; align-items: flex-end; padding: 0 18px 2px;
  }
  .trophy { width: 70px; height: 62px; border-radius: 10px 10px 14px 14px; }
  .trophy--silver { background: linear-gradient(180deg, #b8a6e6, #6b58b0); height: 52px; }
  .trophy--gold { background: linear-gradient(180deg, #f3a52a, #c8561a); width: 82px; height: 66px; }
  .trophy--bronze { background: linear-gradient(180deg, #f59a2c, #d04a1c); height: 54px; }
  .shelf {
    position: absolute; left: 0; top: 204px; width: 330px; height: 8px;
    background: linear-gradient(180deg, #b87a2a, #5a3512);
  }
  .stats {
    position: absolute; left: 0; top: 212px; width: 330px; height: 68px;
    background: var(--band);
    display: flex; align-items: center;
  }
  .stat { flex: 1; text-align: center; position: relative; }
  .stat + .stat::before {
    content: ""; position: absolute; left: 0; top: 6px; width: 1px; height: 40px;
    background: linear-gradient(180deg, transparent, #555, transparent);
  }
  .stat-value { font-size: 23px; font-weight: 500; color: var(--gold); line-height: 1; }
  .stat-label { font-size: 8.5px; color: var(--muted); margin-top: 7px; }
  .muscles {
    position: absolute; left: 0; top: 280px; width: 330px; height: 310px;
    background: var(--panel);
  }
  .muscles-title {
    position: absolute; left: 0; right: 0; top: 27px;
    text-align: center; font-size: 14.5px; font-weight: 500; color: var(--text-light);
  }
  .muscles-title svg { vertical-align: -3px; margin-left: 9px; }
  .body-map {
    position: absolute; left: 22px; top: 80px; width: 286px; height: 204px;
    border-radius: 8px;
    background: linear-gradient(180deg, #3a3420 0%, #2d2d2d 55%, #302a18 100%);
  }
  .features {
    position: absolute; left: 11px; top: 611px; width: 308px;
    display: grid; grid-template-columns: 144px 144px; column-gap: 20px; row-gap: 15px;
  }
  .feature-button {
    height: 40px; border-radius: 5px; border: none;
    background: linear-gradient(180deg, var(--gold-light), var(--gold-deep));
    font-family: "Montserrat", sans-serif; font-size: 11px; font-weight: 500; color: var(--ink);
  }
</style>
</head>
<body>
  <main class="screen">
    <section class="header">
      <div class="status-bar">
        <span>5:50 am</span>
        <span class="status-icons">
          <svg width="11" height="8" viewBox="0 0 11 8"><path d="M5.5 8 L8 5 A4 4 0 0 0 3 5 Z M1 3 A6.5 6.5 0 0 1 10 3" fill="#1d1a12" stroke="#1d1a12" stroke-width="1.2"/></svg>
          <svg width="9" height="8" viewBox="0 0 9 8"><rect x="0" y="5" width="2" height="3" fill="#1d1a12"/><rect x="3.5" y="3" width="2" height="5" fill="#1d1a12"/><rect x="7" y="0" width="2" height="8" fill="#1d1a12"/></svg>
          <svg width="12" height="8" viewBox="0 0 12 8"><rect x="0.5" y="0.5" width="10" height="7" rx="1" fill="none" stroke="#1d1a12"/><rect x="2" y="2" width="7" height="4" fill="#1d1a12"/></svg>
        </span>
      </div>
      <div class="notch"></div>
      <div class="avatar" role="img" aria-label="Profile photo of the user"></div>
      <p class="profile-name">@Dana Morrow</p>
      <p class="profile-location">218 Linden Bay Town</p>
      <svg class="settings" width="18" height="18" viewBox="0 0 24 24" fill="none" stroke="#1d1a12" stroke-width="1.8">
        <circle cx="12" cy="12" r="3.2"/>
        <path d="M12 2.5v3M12 18.5v3M2.5 12h3M18.5 12h3M5.3 5.3l2.1 2.1M16.6 16.6l2.1 2.1M5.3 18.7l2.1-2.1M16.6 7.4l2.1-2.1"/>
        <circle cx="12" cy="12" r="7"/>
      </svg>
      <div class="trophy-case">
        <div class="trophy trophy--silver" role="img" aria-label="Silver trophy"></div>
        <div class="trophy trophy--gold" role="img" aria-label="Gold trophy"></div>
        <div class="trophy trophy--bronze" role="img" aria-label="Bronze trophy"></div>
      </div>
      <div class="shelf"></div>
    </section>

    <section class="stats">
      <div class="stat"><div class="stat-value">38</div><div class="stat-label">Followers</div></div>
      <div class="stat"><div class="stat-value">4</div><div class="stat-label">Trophies</div></div>
      <div class="stat"><div class="stat-value">1</div><div class="stat-label">Medals</div></div>
      <div class="stat"><div class="stat-value">107</div><div class="stat-label">Workouts</div></div>
    </section>

    <section class="muscles">
      <h2 class="muscles-title">Muscles Worked - 7D
        <svg width="15" height="15" viewBox="0 0 16 16"><circle cx="8" cy="8" r="8" fill="#f5b70f"/><path d="M4.5 8h6M8 5.5 10.5 8 8 10.5" stroke="#1d1a12" stroke-width="1.4" fill="none"/></svg>
      </h2>
      <div class="body-map" role="img" aria-label="Front, back and side body outlines with chest, abs, shoulders, arms and calves highlighted in gold"></div>
    </section>

    <nav class="features">
      <button class="feature-button">Strength Review</button>
      <button class="feature-button">Food Logging</button>
      <button class="feature-button">Start Workout</button>
      <button class="feature-button">View Statistics</button>
      <button class="feature-button">AI From Review Tool</button>
      <button class="feature-button">Ask FitKestra AI</button>
    </nav>
  </main>
</body>
</html>
```